MediDesk 4.2 is web based clinic management software. We require 1 logo for the software product, login page design and landing page (patient queue) design. The design should include all elements required logo, icons , buttons and type faces. http://md2021.tralvonix.my/Default.aspxTest login : KQ417 password : 4826 Final output should be in psd for developer to convert to css for web application.

Number of Pages Required

1 page

Colors

Designer to choose colors to be used in the design.

Requirements
Must have
• Product Logo , icon, login page design, and 1 main page design as attached.

```html
<!DOCTYPE html>
<html lang="en">
<head>
<meta charset="utf-8">
<title>MediDesk 4.2 – Login and Patient Queue</title>
<link rel="stylesheet" href="https://fonts.googleapis.com/css2?family=Nunito+Sans:wght@400;600;700&display=swap">
<style>
:root{
  --board-top:#33094a;
  --board-bottom:#1b0d50;
  --mint:#cde8c6;
  --sage:#b9dcc0;
  --teal:#6d9eaa;
  --teal-deep:#5e919e;
  --ink:#111418;
  --navy:#1d4a66;
  --brand-blue:#1f5d9e;
  --accent-blue:#2f8bd6;
  --button-blue:#4a74ad;
  --header-bar:#b3d0d5;
  --pill:#b5d8cf;
  --logout:#b5172b;
  --rule:#b9cfd6;
  --white:#ffffff;
}
*{box-sizing:border-box;margin:0;padding:0}
html,body{width:800px;height:1200px;overflow:hidden}
body{
  font-family:"Nunito Sans",Arial,sans-serif;
  background:radial-gradient(ellipse at 80% 10%,#3a0848 0%,transparent 55%),
             linear-gradient(180deg,var(--board-top) 0%,#250b4d 50%,var(--board-bottom) 100%);
  position:relative;color:var(--ink);
}
.screen{position:absolute;overflow:hidden;box-shadow:0 4px 14px rgba(0,0,0,.35)}

/* Login screen */
.screen--login{left:114px;top:52px;width:571px;height:321px;
  background:linear-gradient(35deg,var(--teal) 0%,#8fb6b5 45%,var(--mint) 100%)}
.login-card{position:absolute;left:202px;top:54px;width:166px;height:214px;
  background:rgba(170,200,205,.55);border-radius:3px}
.brand{position:absolute;display:flex;align-items:center;gap:4px;white-space:nowrap;transform:translateX(-50%)}
.brand__name{font-weight:600;letter-spacing:-.2px}
.brand__dot{border-radius:50%;background:var(--accent-blue)}
.login-card .brand{left:83px;top:24px}
.login-card .brand__name{font-size:16px;color:var(--brand-blue)}
.login-card .brand__dot{width:9px;height:9px}
.field{position:absolute;left:31px;width:105px;border-bottom:1px solid #eef4f5;
  font-size:6px;color:#1e4c66;text-align:center;padding-bottom:1px}
.field--user{top:74px}
.field--pass{top:118px}
.btn-login{position:absolute;left:48px;top:147px;width:71px;height:16px;border-radius:8px;
  background:var(--button-blue);color:var(--white);font-size:8.5px;display:flex;align-items:center;justify-content:center;letter-spacing:.2px}
.link-clear{position:absolute;left:135px;top:165px;font-size:4.5px;color:#3d5e6a}

/* Queue screen */
.screen--queue{left:115px;top:439px;width:572px;height:322px;
  background:linear-gradient(180deg,var(--mint) 0%,var(--sage) 35%,#97c0b8 65%,var(--teal-deep) 100%)}
.menu-toggle{position:absolute;left:71px;top:10px;width:18px;height:11px}
.screen .brand--header{left:283px;top:6px}
.brand--header .brand__name{font-size:11px;color:var(--navy)}
.brand--header .brand__dot{width:7px;height:7px;background:var(--navy)}
.datetime{position:absolute;right:73px;top:9px;font-size:6px;line-height:8px;text-align:right;color:var(--ink)}
.filter{position:absolute;top:55px;width:67px;height:13px;border-radius:7px;background:var(--pill);
  font-size:5.6px;color:#2a4a58;display:flex;align-items:center;justify-content:center;gap:6px}
.filter svg{width:9px;height:5px}
.filter--date{left:202px}
.filter--location{left:284px}
.queue-title{position:absolute;left:71px;top:94px;font-size:5.8px;font-weight:700}
.search{position:absolute;left:486px;top:89px;width:12px;height:12px;border-radius:50%;background:#a9d3ae;display:flex;align-items:center;justify-content:center}
.search svg{width:8px;height:8px}

.queue-table{position:absolute;left:68px;top:107px;width:436px}
.queue-head,.queue-row{display:grid;grid-template-columns:20px 58px 56px 36px 44px 42px 41px 45px 33px 1fr;align-items:center;padding-left:6px}
.queue-head{height:12px;border-radius:6px;background:var(--header-bar);font-size:5.6px;font-weight:600}
.queue-body{margin:0 3px;background:var(--white);padding-top:2px}
.queue-row{height:16.6px;font-size:5.6px;font-weight:700}
.queue-row .icons{display:flex;gap:3px}
.icon{width:7.5px;height:7.5px;color:var(--ink)}
.icon--payor{width:9px;height:10px}
.cell-center{text-align:center}

/* Menu drawer screen */
.screen--menu{left:115px;top:851px;width:570px;height:321px;
  background:linear-gradient(180deg,var(--mint) 0%,var(--sage) 35%,#97c0b8 65%,var(--teal-deep) 100%)}
.faded{position:absolute;inset:0;opacity:.22}
.drawer{position:absolute;left:68px;top:0;width:178px;height:321px;background:var(--white)}
.drawer__close{position:absolute;left:163px;top:6px;font-size:7px}
.avatar{position:absolute;left:71px;top:20px;width:40px;height:40px;border-radius:50%;
  background:radial-gradient(circle at 50% 40%,#e9ddd6 0%,#c9b1a6 55%,#efe9e6 100%)}
.drawer__name{position:absolute;left:0;width:178px;top:65px;text-align:center;font-size:9px;font-weight:600}
.drawer__role{position:absolute;left:0;width:178px;top:76px;text-align:center;font-size:4.4px;color:var(--accent-blue);letter-spacing:.3px}
.btn-logout{position:absolute;left:70px;top:89px;width:39px;height:11px;border-radius:6px;background:var(--logout);
  color:var(--white);font-size:6px;display:flex;align-items:center;justify-content:center}
.rule{position:absolute;left:10px;width:156px;height:1px;background:var(--rule)}
.nav{position:absolute;left:10px;top:119px;list-style:none}
.nav li{display:flex;align-items:center;height:15px;font-size:5.8px;gap:8px}
.nav svg{width:8px;height:7px}
.sub-nav{position:absolute;left:12px;top:196px;list-style:none}
.sub-nav li{font-size:5.8px;height:13px}
</style>
</head>
<body>

<svg width="0" height="0" style="position:absolute" aria-hidden="true">
  <defs>
    <symbol id="i-person" viewBox="0 0 12 12"><circle cx="6" cy="3.2" r="2.6" fill="currentColor"/><path d="M1 12c0-3.5 2.2-5 5-5s5 1.5 5 5z" fill="currentColor"/></symbol>
    <symbol id="i-clip" viewBox="0 0 12 12"><rect x="2" y="2" width="8" height="9.5" rx="1" fill="none" stroke="currentColor"/><rect x="4" y="1" width="4" height="2" fill="currentColor"/><path d="M4 6h4M4 8h3" stroke="currentColor" stroke-width=".8"/></symbol>
    <symbol id="i-case" viewBox="0 0 12 12"><rect x="1" y="4" width="10" height="7" rx="1" fill="none" stroke="currentColor"/><path d="M4 4V2.5h4V4M1 7h10" fill="none" stroke="currentColor"/></symbol>
    <symbol id="i-doc" viewBox="0 0 12 12"><path d="M2.5 1h5l2.5 2.5V11h-7.5z" fill="none" stroke="currentColor"/><path d="M4 5h4M4 7h4M4 9h3" stroke="currentColor" stroke-width=".7"/></symbol>
    <symbol id="i-building" viewBox="0 0 12 14"><path d="M2 13V1h6v12M8 5h3v8M1 13h11" fill="none" stroke="currentColor" stroke-width=".9"/><path d="M3.5 3h1M5.5 3h1M3.5 5.5h1M5.5 5.5h1M3.5 8h1M5.5 8h1M3.5 10.5h1M5.5 10.5h1M9 7.5h1M9 10h1" stroke="currentColor"/></symbol>
    <symbol id="i-hourglass" viewBox="0 0 12 12"><path d="M2.5 1h7M2.5 11h7M3.5 1c0 3 5 3 5 5s-5 2-5 5M8.5 1c0 3-5 3-5 5s5 2 5 5" fill="none" stroke="currentColor"/></symbol>
    <symbol id="i-clock" viewBox="0 0 12 12"><circle cx="6" cy="6" r="5" fill="none" stroke="currentColor" stroke-width="1.1"/><path d="M6 3v3.2l2 1.3" fill="none" stroke="currentColor"/></symbol>
    <symbol id="i-edit" viewBox="0 0 12 12"><rect x="1.5" y="1.5" width="7.5" height="9.5" fill="none" stroke="currentColor"/><path d="M3 4h4M3 6h3M6 10l4.5-5 1 1L7 11H6z" fill="none" stroke="currentColor" stroke-width=".8"/></symbol>
    <symbol id="i-steth" viewBox="0 0 12 12"><path d="M3 1v3a2.5 2.5 0 0 0 5 0V1M5.5 6.5V9a2 2 0 0 0 4 0V7.5" fill="none" stroke="currentColor"/><circle cx="9.5" cy="6.5" r="1.2" fill="none" stroke="currentColor"/></symbol>
    <symbol id="i-chev" viewBox="0 0 10 6"><path d="M1 1l4 4 4-4" fill="none" stroke="currentColor" stroke-width=".8"/></symbol>
  </defs>
</svg>

<!-- Login -->
<section class="screen screen--login">
  <div class="login-card">
    <div class="brand"><span class="brand__name">MediDesk</span><span class="brand__dot"></span></div>
    <div class="field field--user">Username</div>
    <div class="field field--pass">Password</div>
    <div class="btn-login">LOG IN</div>
    <div class="link-clear">Clear</div>
  </div>
</section>

<!-- Patient queue -->
<section class="screen screen--queue">
  <svg class="menu-toggle" viewBox="0 0 18 11"><path d="M0 1h18M0 5.5h18M0 10h18" stroke="#1d4a66" stroke-width="1.8"/></svg>
  <div class="brand brand--header"><span class="brand__name">MediDesk</span><span class="brand__dot"></span></div>
  <div class="datetime">22. October 2018<br>01:00 PM</div>
  <div class="filter filter--date">Que Date <svg><use href="#i-chev"/></svg></div>
  <div class="filter filter--location">Que Location <svg><use href="#i-chev"/></svg></div>
  <div class="queue-title">Patients in que (20)</div>
  <div class="search"><svg viewBox="0 0 10 10"><circle cx="4" cy="4" r="3" fill="none" stroke="#3f7a4f"/><path d="M6.2 6.2L9 9" stroke="#3f7a4f"/></svg></div>

  <div class="queue-table">
    <div class="queue-head"><span>No.</span><span></span><span>Full Name</span><span></span><span class="cell-center">Arrived</span><span class="cell-center">Payor</span><span class="cell-center">Amount</span><span class="cell-center">Doctor</span><span>Location</span><span></span></div>
    <div class="queue-body">
      <div class="queue-row"><span>1</span><span class="icons"><svg class="icon"><use href="#i-person"/></svg><svg class="icon"><use href="#i-clip"/></svg><svg class="icon"><use href="#i-case"/></svg><svg class="icon"><use href="#i-doc"/></svg></span><span>Dana Whitlow</span><span>26 ♂</span><span class="cell-center">12:00</span><span class="cell-center"><svg class="icon icon--payor"><use href="#i-building"/></svg></span><span class="cell-center">$100</span><span class="cell-center">D0089</span><span>R12</span><span class="icons"><svg class="icon"><use href="#i-hourglass"/></svg><svg class="icon"><use href="#i-clock"/></svg><svg class="icon"><use href="#i-edit"/></svg><svg class="icon"><use href="#i-steth"/></svg></span></div>
      <div class="queue-row"><span>1</span><span class="icons"><svg class="icon"><use href="#i-person"/></svg><svg class="icon"><use href="#i-clip"/></svg><svg class="icon"><use href="#i-case"/></svg><svg class="icon"><use href="#i-doc"/></svg></span><span>Dana Whitlow</span><span>26 ♂</span><span class="cell-center">12:00</span><span class="cell-center"><svg class="icon icon--payor"><use href="#i-building"/></svg></span><span class="cell-center">$100</span><span class="cell-center">D0089</span><span>R12</span><span class="icons"><svg class="icon"><use href="#i-hourglass"/></svg><svg class="icon"><use href="#i-clock"/></svg><svg class="icon"><use href="#i-edit"/></svg><svg class="icon"><use href="#i-steth"/></svg></span></div>
      <div class="queue-row"><span>1</span><span class="icons"><svg class="icon"><use href="#i-person"/></svg><svg class="icon"><use href="#i-clip"/></svg><svg class="icon"><use href="#i-case"/></svg><svg class="icon"><use href="#i-doc"/></svg></span><span>Dana Whitlow</span><span>26 ♂</span><span class="cell-center">12:00</span><span class="cell-center"><svg class="icon icon--payor"><use href="#i-building"/></svg></span><span class="cell-center">$100</span><span class="cell-center">D0089</span><span>R12</span><span class="icons"><svg class="icon"><use href="#i-hourglass"/></svg><svg class="icon"><use href="#i-clock"/></svg><svg class="icon"><use href="#i-edit"/></svg><svg class="icon"><use href="#i-steth"/></svg></span></div>
      <div class="queue-row"><span>1</span><span class="icons"><svg class="icon"><use href="#i-person"/></svg><svg class="icon"><use href="#i-clip"/></svg><svg class="icon"><use href="#i-case"/></svg><svg class="icon"><use href="#i-doc"/></svg></span><span>Dana Whitlow</span><span>26 ♂</span><span class="cell-center">12:00</span><span class="cell-center"><svg class="icon icon--payor"><use href="#i-building"/></svg></span><span class="cell-center">$100</span><span class="cell-center">D0089</span><span>R12</span><span class="icons"><svg class="icon"><use href="#i-hourglass"/></svg><svg class="icon"><use href="#i-clock"/></svg><svg class="icon"><use href="#i-edit"/></svg><svg class="icon"><use href="#i-steth"/></svg></span></div>
      <div class="queue-row"><span>1</span><span class="icons"><svg class="icon"><use href="#i-person"/></svg><svg class="icon"><use href="#i-clip"/></svg><svg class="icon"><use href="#i-case"/></svg><svg class="icon"><use href="#i-doc"/></svg></span><span>Dana Whitlow</span><span>26 ♂</span><span class="cell-center">12:00</span><span class="cell-center"><svg class="icon icon--payor"><use href="#i-building"/></svg></span><span class="cell-center">$100</span><span class="cell-center">D0089</span><span>R12</span><span class="icons"><svg class="icon"><use href="#i-hourglass"/></svg><svg class="icon"><use href="#i-clock"/></svg><svg class="icon"><use href="#i-edit"/></svg><svg class="icon"><use href="#i-steth"/></svg></span></div>
      <div class="queue-row"><span>1</span><span class="icons"><svg class="icon"><use href="#i-person"/></svg><svg class="icon"><use href="#i-clip"/></svg><svg class="icon"><use href="#i-case"/></svg><svg class="icon"><use href="#i-doc"/></svg></span><span>Dana Whitlow</span><span>26 ♂</span><span class="cell-center">12:00</span><span class="cell-center"><svg class="icon icon--payor"><use href="#i-building"/></svg></span><span class="cell-center">$100</span><span class="cell-center">D0089</span><span>R12</span><span class="icons"><svg class="icon"><use href="#i-hourglass"/></svg><svg class="icon"><use href="#i-clock"/></svg><svg class="icon"><use href="#i-edit"/></svg><svg class="icon"><use href="#i-steth"/></svg></span></div>
      <div class="queue-row"><span>1</span><span class="icons"><svg class="icon"><use href="#i-person"/></svg><svg class="icon"><use href="#i-clip"/></svg><svg class="icon"><use href="#i-case"/></svg><svg class="icon"><use href="#i-doc"/></svg></span><span>Dana Whitlow</span><span>26 ♂</span><span class="cell-center">12:00</span><span class="cell-center"><svg class="icon icon--payor"><use href="#i-building"/></svg></span><span class="cell-center">$100</span><span class="cell-center">D0089</span><span>R12</span><span class="icons"><svg class="icon"><use href="#i-hourglass"/></svg><svg class="icon"><use href="#i-clock"/></svg><svg class="icon"><use href="#i-edit"/></svg><svg class="icon"><use href="#i-steth"/></svg></span></div>
      <div class="queue-row"><span>1</span><span class="icons"><svg class="icon"><use href="#i-person"/></svg><svg class="icon"><use href="#i-clip"/></svg><svg class="icon"><use href="#i-case"/></svg><svg class="icon"><use href="#i-doc"/></svg></span><span>Dana Whitlow</span><span>26 ♂</span><span class="cell-center">12:00</span><span class="cell-center"><svg class="icon icon--payor"><use href="#i-building"/></svg></span><span class="cell-center">$100</span><span class="cell-center">D0089</span><span>R12</span><span class="icons"><svg class="icon"><use href="#i-hourglass"/></svg><svg class="icon"><use href="#i-clock"/></svg><svg class="icon"><use href="#i-edit"/></svg><svg class="icon"><use href="#i-steth"/></svg></span></div>
      <div class="queue-row"><span>1</span><span class="icons"><svg class="icon"><use href="#i-person"/></svg><svg class="icon"><use href="#i-clip"/></svg><svg class="icon"><use href="#i-case"/></svg><svg class="icon"><use href="#i-doc"/></svg></span><span>Dana Whitlow</span><span>26 ♂</span><span class="cell-center">12:00</span><span class="cell-center"><svg class="icon icon--payor"><use href="#i-building"/></svg></span><span class="cell-center">$100</span><span class="cell-center">D0089</span><span>R12</span><span class="icons"><svg class="icon"><use href="#i-hourglass"/></svg><svg class="icon"><use href="#i-clock"/></svg><svg class="icon"><use href="#i-edit"/></svg><svg class="icon"><use href="#i-steth"/></svg></span></div>
      <div class="queue-row"><span>1</span><span class="icons"><svg class="icon"><use href="#i-person"/></svg><svg class="icon"><use href="#i-clip"/></svg><svg class="icon"><use href="#i-case"/></svg><svg class="icon"><use href="#i-doc"/></svg></span><span>Dana Whitlow</span><span>26 ♂</span><span class="cell-center">12:00</span><span class="cell-center"><svg class="icon icon--payor"><use href="#i-building"/></svg></span><span class="cell-center">$100</span><span class="cell-center">D0089</span><span>R12</span><span class="icons"><svg class="icon"><use href="#i-hourglass"/></svg><svg class="icon"><use href="#i-clock"/></svg><svg class="icon"><use href="#i-edit"/></svg><svg class="icon"><use href="#i-steth"/></svg></span></div>
      <div class="queue-row"><span>1</span><span class="icons"><svg class="icon"><use href="#i-person"/></svg><svg class="icon"><use href="#i-clip"/></svg><svg class="icon"><use href="#i-case"/></svg><svg class="icon"><use href="#i-doc"/></svg></span><span>Dana Whitlow</span><span>26 ♂</span><span class="cell-center">12:00</span><span class="cell-center"><svg class="icon icon--payor"><use href="#i-building"/></svg></span><span class="cell-center">$100</span><span class="cell-center">D0089</span><span>R12</span><span class="icons"><svg class="icon"><use href="#i-hourglass"/></svg><svg class="icon"><use href="#i-clock"/></svg><svg class="icon"><use href="#i-edit"/></svg><svg class="icon"><use href="#i-steth"/></svg></span></div>
      <div class="queue-row"><span>1</span><span class="icons"><svg class="icon"><use href="#i-person"/></svg><svg class="icon"><use href="#i-clip"/></svg><svg class="icon"><use href="#i-case"/></svg><svg class="icon"><use href="#i-doc"/></svg></span><span>Dana Whitlow</span><span>26 ♂</span><span class="cell-center">12:00</span><span class="cell-center"><svg class="icon icon--payor"><use href="#i-building"/></svg></span><span class="cell-center">$100</span><span class="cell-center">D0089</span><span>R12</span><span class="icons"><svg class="icon"><use href="#i-hourglass"/></svg><svg class="icon"><use href="#i-clock"/></svg><svg class="icon"><use href="#i-edit"/></svg><svg class="icon"><use href="#i-steth"/></svg></span></div>
    </div>
  </div>
</section>

<!-- Queue with open menu drawer -->
<section class="screen screen--menu">
  <div class="faded">
    <div class="brand brand--header"><span class="brand__name">MediDesk</span><span class="brand__dot"></span></div>
    <div class="datetime">22. October 2018<br>01:00 PM</div>
    <div class="filter filter--location">Que Location <svg><use href="#i-chev"/></svg></div>
    <div class="search"><svg viewBox="0 0 10 10"><circle cx="4" cy="4" r="3" fill="none" stroke="#3f7a4f"/><path d="M6.2 6.2L9 9" stroke="#3f7a4f"/></svg></div>
    <div class="queue-table">
      <div class="queue-head"><span></span><span></span><span></span><span></span><span class="cell-center">Arrived</span><span class="cell-center">Payor</span><span class="cell-center">Amount</span><span class="cell-center">Doctor</span><span>Location</span><span></span></div>
      <div class="queue-body">
        <div class="queue-row"><span></span><span></span><span></span><span></span><span class="cell-center">12:00</span><span class="cell-center"><svg class="icon icon--payor"><use href="#i-building"/></svg></span><span class="cell-center">$100</span><span class="cell-center">D0089</span><span>R12</span><span class="icons"><svg class="icon"><use href="#i-hourglass"/></svg><svg class="icon"><use href="#i-clock"/></svg><svg class="icon"><use href="#i-edit"/></svg><svg class="icon"><use href="#i-steth"/></svg></span></div>
        <div class="queue-row"><span></span><span></span><span></span><span></span><span class="cell-center">12:00</span><span class="cell-center"><svg class="icon icon--payor"><use href="#i-building"/></svg></span><span class="cell-center">$100</span><span class="cell-center">D0089</span><span>R12</span><span class="icons"><svg class="icon"><use href="#i-hourglass"/></svg><svg class="icon"><use href="#i-clock"/></svg><svg class="icon"><use href="#i-edit"/></svg><svg class="icon"><use href="#i-steth"/></svg></span></div>
        <div class="queue-row"><span></span><span></span><span></span><span></span><span class="cell-center">12:00</span><span class="cell-center"><svg class="icon icon--payor"><use href="#i-building"/></svg></span><span class="cell-center">$100</span><span class="cell-center">D0089</span><span>R12</span><span class="icons"><svg class="icon"><use href="#i-hourglass"/></svg><svg class="icon"><use href="#i-clock"/></svg><svg class="icon"><use href="#i-edit"/></svg><svg class="icon"><use href="#i-steth"/></svg></span></div>
        <div class="queue-row"><span></span><span></span><span></span><span></span><span class="cell-center">12:00</span><span class="cell-center"><svg class="icon icon--payor"><use href="#i-building"/></svg></span><span class="cell-center">$100</span><span class="cell-center">D0089</span><span>R12</span><span class="icons"><svg class="icon"><use href="#i-hourglass"/></svg><svg class="icon"><use href="#i-clock"/></svg><svg class="icon"><use href="#i-edit"/></svg><svg class="icon"><use href="#i-steth"/></svg></span></div>
        <div class="queue-row"><span></span><span></span><span></span><span></span><span class="cell-center">12:00</span><span class="cell-center"><svg class="icon icon--payor"><use href="#i-building"/></svg></span><span class="cell-center">$100</span><span class="cell-center">D0089</span><span>R12</span><span class="icons"><svg class="icon"><use href="#i-hourglass"/></svg><svg class="icon"><use href="#i-clock"/></svg><svg class="icon"><use href="#i-edit"/></svg><svg class="icon"><use href="#i-steth"/></svg></span></div>
        <div class="queue-row"><span></span><span></span><span></span><span></span><span class="cell-center">12:00</span><span class="cell-center"><svg class="icon icon--payor"><use href="#i-building"/></svg></span><span class="cell-center">$100</span><span class="cell-center">D0089</span><span>R12</span><span class="icons"><svg class="icon"><use href="#i-hourglass"/></svg><svg class="icon"><use href="#i-clock"/></svg><svg class="icon"><use href="#i-edit"/></svg><svg class="icon"><use href="#i-steth"/></svg></span></div>
        <div class="queue-row"><span></span><span></span><span></span><span></span><span class="cell-center">12:00</span><span class="cell-center"><svg class="icon icon--payor"><use href="#i-building"/></svg></span><span class="cell-center">$100</span><span class="cell-center">D0089</span><span>R12</span><span class="icons"><svg class="icon"><use href="#i-hourglass"/></svg><svg class="icon"><use href="#i-clock"/></svg><svg class="icon"><use href="#i-edit"/></svg><svg class="icon"><use href="#i-steth"/></svg></span></div>
        <div class="queue-row"><span></span><span></span><span></span><span></span><span class="cell-center">12:00</span><span class="cell-center"><svg class="icon icon--payor"><use href="#i-building"/></svg></span><span class="cell-center">$100</span><span class="cell-center">D0089</span><span>R12</span><span class="icons"><svg class="icon"><use href="#i-hourglass"/></svg><svg class="icon"><use href="#i-clock"/></svg><svg class="icon"><use href="#i-edit"/></svg><svg class="icon"><use href="#i-steth"/></svg></span></div>
        <div class="queue-row"><span></span><span></span><span></span><span></span><span class="cell-center">12:00</span><span class="cell-center"><svg class="icon icon--payor"><use href="#i-building"/></svg></span><span class="cell-center">$100</span><span class="cell-center">D0089</span><span>R12</span><span class="icons"><svg class="icon"><use href="#i-hourglass"/></svg><svg class="icon"><use href="#i-clock"/></svg><svg class="icon"><use href="#i-edit"/></svg><svg class="icon"><use href="#i-steth"/></svg></span></div>
        <div class="queue-row"><span></span><span></span><span></span><span></span><span class="cell-center">12:00</span><span class="cell-center"><svg class="icon icon--payor"><use href="#i-building"/></svg></span><span class="cell-center">$100</span><span class="cell-center">D0089</span><span>R12</span><span class="icons"><svg class="icon"><use href="#i-hourglass"/></svg><svg class="icon"><use href="#i-clock"/></svg><svg class="icon"><use href="#i-edit"/></svg><svg class="icon"><use href="#i-steth"/></svg></span></div>
        <div class="queue-row"><span></span><span></span><span></span><span></span><span class="cell-center">12:00</span><span class="cell-center"><svg class="icon icon--payor"><use href="#i-building"/></svg></span><span class="cell-center">$100</span><span class="cell-center">D0089</span><span>R12</span><span class="icons"><svg class="icon"><use href="#i-hourglass"/></svg><svg class="icon"><use href="#i-clock"/></svg><svg class="icon"><use href="#i-edit"/></svg><svg class="icon"><use href="#i-steth"/></svg></span></div>
        <div class="queue-row"><span></span><span></span><span></span><span></span><span class="cell-center">12:00</span><span class="cell-center"><svg class="icon icon--payor"><use href="#i-building"/></svg></span><span class="cell-center">$100</span><span class="cell-center">D0089</span><span>R12</span><span class="icons"><svg class="icon"><use href="#i-hourglass"/></svg><svg class="icon"><use href="#i-clock"/></svg><svg class="icon"><use href="#i-edit"/></svg><svg class="icon"><use href="#i-steth"/></svg></span></div>
      </div>
    </div>
  </div>

  <aside class="drawer">
    <div class="drawer__close">×</div>
    <div class="avatar" role="img" aria-label="Portrait photo of the signed-in doctor"></div>
    <div class="drawer__name">Dr. Maren Holt</div>
    <div class="drawer__role">KARDIOLOGIST</div>
    <div class="btn-logout">LOG OUT</div>
    <div class="rule" style="top:109px"></div>
    <ul class="nav">
      <li><svg viewBox="0 0 8 7"><path d="M0 1h1M2 1h6M0 3.5h1M2 3.5h6M0 6h1M2 6h6" stroke="#111" stroke-width=".8"/></svg>Queue</li>
      <li><svg viewBox="0 0 8 7"><circle cx="3" cy="2" r="1.5" fill="#111"/><circle cx="6" cy="2.3" r="1.2" fill="#111"/><path d="M0 7c0-2 1.3-3 3-3s3 1 3 3zM5.5 4.2c1.5 0 2.5.8 2.5 2.5H6.5" fill="#111"/></svg>Patients</li>
      <li><svg viewBox="0 0 8 7"><rect x=".5" y="1" width="7" height="5.5" fill="none" stroke="#111" stroke-width=".7"/><path d="M.5 2.5h7M2 0v1.5M6 0v1.5M2 4h1M4 4h1M2 5.3h1M4 5.3h1" stroke="#111" stroke-width=".6"/></svg>Visit Entry</li>
      <li><svg viewBox="0 0 8 7"><rect x=".5" y="1" width="7" height="5" rx=".5" fill="none" stroke="#111" stroke-width=".7"/><path d="M.5 2.6h7" stroke="#111" stroke-width="1.1"/></svg>Payments</li>
    </ul>
    <div class="rule" style="top:183px"></div>
    <ul class="sub-nav">
      <li>Clinic Information</li>
      <li>Branch Information</li>
    </ul>
    <div class="rule" style="top:229px"></div>
  </aside>
</section>

</body>
</html>
```